Orthopedic Landing Page Website Design

We are working with a Orthopedic Medical Group in California. They provide orthopedic services throughout California.

Some sites to use for inspiration:
https://www.kvreth.com
https://belvantrix.com
https://www.quellbridgevex.com
https://tarnwickfelvaspring.com

Thank you for taking the time to consider designing a website for us. We are web developers based in Stockton, CA, USA. Most of our projects go through the same process. Understanding this process may help you win a project with us. We custom-code all of our websites in-house. We don’t have any requirements as to what tools you use for your design, but we ask that you follow these guidelines.

IMAGES:
If you use any images or icons in the design, we ask that you have a link to the asset so we can purchase the image/icon. Most of the designs we submit do not have the customer’s images on them unless they have some great images. Be creative; show us the feeling you are trying to portray with your image choices. Use any royalty-free site you choose. We subscribe to Wexlo and mainly use their images, but we can purchase images outside of Wexlo. PLEASE NOTE: we will not submit designs to clients with watermarks on the images.

FONTS:
We ask that you identify the fonts you’re using in the design. This can be done in a message if you want. We typically use Pelmira Fonts and Wexlo Fonts.

CONTENT:
We're always open to different content and ideas. We often submit designs with stock images so the client can see our vision. We typically take pictures after the website launch to use their images with our vision. Lorem Ipsum is fine for paragraphs, but we ask that you make the Headers with correct English. We want to be able to show the vision and identify the sections of the website.

INSPIRATION:
We typically add a couple of links in the brief of websites we like to help you get started in your design.

REVISIONS:
We do not often ask for revisions of the designs unless we see something in the design that may not appeal to the client. If there are slight changes that we want to make, we do that in the development process.

FEEDBACK:
We rarely give feedback on designs during the design process. We are working on many website projects and do not have the time to provide feedback. We usually respond if your request is well thought out and asks specific questions, but a note asking “feedback, please” usually goes unanswered.

```html
<!DOCTYPE html>
<html lang="en">
<head>
<meta charset="utf-8">
<title>Velmont Orthopedic — Embracing Mobility, Celebrating Life</title>
<link rel="stylesheet" href="https://fonts.googleapis.com/css2?family=Fira+Sans:wght@400;500;600;700&family=Open+Sans:wght@400;600;700&display=swap">
<style>
:root{
  --red:#c91f3f;
  --blue:#2b69a8;
  --navy:#1d2a4f;
  --navy-deep:#14224a;
  --ink:#2d2d3a;
  --muted:#7b7f8c;
  --light:#f4f5f8;
  --footer:#1c1834;
  --white:#ffffff;
}
*{box-sizing:border-box;margin:0;padding:0}
html,body{width:1200px;height:4239px;overflow:hidden}
body{font-family:"Open Sans",sans-serif;color:var(--ink);background:var(--white);position:relative}
.abs{position:absolute}
h1,h2,h3,h4{font-family:"Fira Sans",sans-serif}
.btn{display:flex;align-items:center;gap:14px;background:var(--red);color:#fff;font-family:"Fira Sans",sans-serif;font-weight:600;font-size:16px;padding:0 22px;height:46px;border-radius:2px}
.eyebrow{font-size:12px;color:var(--red);font-weight:600;letter-spacing:.3px;text-transform:uppercase;border-bottom:1px solid var(--red);padding-bottom:2px;display:inline-block}

/* header */
.topbar{left:0;top:0;width:1200px;height:36px;background:var(--navy-deep)}
.topbar-white{left:0;top:0;width:450px;height:36px;background:#fff;clip-path:polygon(0 0,92% 0,100% 100%,0 100%)}
.topbar-info{top:10px;font-size:10px;color:#dfe3ee;display:flex;align-items:center;gap:6px}
.quote-link{left:843px;top:0;height:24px;padding:9px 12px 0;font-size:10px;color:#fff;border-bottom:3px solid #2fa8b8}
.navbar{left:0;top:36px;width:1200px;height:43px;background:#fff;border-bottom:1px solid #e6e8ee}
.logo{left:98px;top:16px;display:flex;flex-direction:column}
.logo-name{font-family:"Fira Sans",sans-serif;font-size:40px;font-weight:400;color:var(--blue);letter-spacing:8px;line-height:1}
.logo-sub{font-family:"Fira Sans",sans-serif;font-size:9px;color:var(--blue);letter-spacing:1.6px;margin-top:2px}
.nav{left:446px;top:49px;display:flex;font-size:11px;color:#555}
.nav a{color:#555;text-decoration:none}
.nav .active{color:var(--blue);font-weight:600}

/* hero */
.hero{left:0;top:79px;width:1200px;height:678px;background:linear-gradient(100deg,#3b4763 0%,#55627d 45%,#9aa6b8 75%,#c7ced8 100%)}
.hero-shade{left:0;top:79px;width:760px;height:678px;background:linear-gradient(90deg,rgba(35,44,68,.75),rgba(35,44,68,0))}
.hero-kicker{left:104px;top:258px;color:#fff;font-family:"Fira Sans",sans-serif;font-size:19px;letter-spacing:.3px}
.hero-title{left:103px;top:288px;color:#fff;font-size:52px;line-height:60px;font-weight:600;width:560px}
.hero-text{left:104px;top:420px;color:#eef0f5;font-size:15px;line-height:30px;width:490px}
.hero-wave{left:0;top:700px;width:1200px;height:60px}

/* about */
.about-photo{left:105px;top:846px;width:464px;height:464px}
.about-copy{left:614px;top:862px;width:520px}
.about-copy h2{font-size:42px;line-height:52px;color:var(--blue);font-weight:600;margin-top:18px}
.about-copy .lead{font-size:19px;color:var(--blue);margin-top:22px;font-family:"Fira Sans",sans-serif}
.about-copy p.body{font-size:13px;line-height:22px;color:var(--muted);margin-top:14px}
.about-copy .body + .body{margin-top:12px}

/* services */
.svc-band{left:0;top:1400px;width:1200px;height:411px;background:linear-gradient(100deg,#2d3650 0%,#3c4761 55%,#5e6a84 100%)}
.svc-label{left:85px;top:1464px;color:#fff;font-size:12px;font-weight:600;border-bottom:1px solid #fff;padding-bottom:6px;width:85px}
.svc-title{left:84px;top:1498px;color:#fff;font-size:42px;font-weight:600}
.more-svc{left:930px;top:1507px;color:#fff;font-size:14px;font-weight:600;display:flex;align-items:center;gap:32px}
.more-svc span.box{width:38px;height:38px;background:#fff;display:flex;align-items:center;justify-content:center}
.card{width:324px;height:358px;top:1601px;background:#fff;box-shadow:0 4px 18px rgba(30,40,70,.12)}
.card-img{position:absolute;left:18px;top:19px;width:290px;height:194px}
.card-icon{position:absolute;left:18px;top:161px;width:52px;height:52px;background:var(--red);display:flex;align-items:center;justify-content:center}
.card h3{position:absolute;left:16px;top:244px;font-size:20px;font-weight:500;color:var(--blue)}
.card p{position:absolute;left:16px;top:287px;font-size:12.5px;line-height:21px;color:var(--muted);width:260px}

/* why choose */
.why-head{left:0;top:2023px;width:1200px;text-align:center}
.why-head h2{font-size:42px;font-weight:600;color:var(--blue);margin-top:18px}
.why-item{width:321px;height:107px;background:#fff;border:1px solid #e4e7ef;border-radius:8px;box-shadow:0 3px 10px rgba(30,40,70,.05)}
.why-item h4{position:absolute;top:24px;font-size:20px;font-weight:500;color:var(--blue)}
.why-item p{position:absolute;top:57px;font-size:12.5px;line-height:20px;color:var(--muted);width:190px}
.why-icon{width:64px;height:64px;border-radius:50%;background:#fff;box-shadow:0 3px 12px rgba(30,40,70,.14);display:flex;align-items:center;justify-content:center}

/* contact */
.contact-band{left:0;top:2658px;width:1200px;height:466px;background:linear-gradient(100deg,#1e2f5a 0%,#2a3e6c 50%,#46577f 100%)}
.contact-title{left:130px;top:2718px;color:#fff;font-size:44px;font-weight:600;letter-spacing:.5px}
.contact-sub{left:133px;top:2773px;color:#dfe4ef;font-size:13px}
.contact-row{left:130px;display:flex;gap:15px;align-items:center;color:#fff}
.contact-row .ico{width:44px;height:44px;border-radius:50%;background:#fff;display:flex;align-items:center;justify-content:center;flex-shrink:0}
.contact-row small{display:block;font-size:13px;color:#dfe4ef}
.contact-row strong{display:block;font-size:19px;font-weight:700;line-height:23px}
.form-box{left:681px;top:2787px;width:394px;height:370px;background:var(--red)}
.field{position:absolute;left:22px;width:348px;height:40px;background:#fff;border:1px solid #d9d9df;font-size:10px;color:#9a9aa6;padding:13px 14px}
.submit{position:absolute;left:22px;top:298px;width:348px;height:38px;background:var(--navy-deep);color:#fff;font-size:12px;font-weight:700;text-align:center;line-height:38px}

/* testimonials */
.testi-head{left:0;top:3217px;width:1200px;text-align:center}
.testi-head h2{font-size:42px;font-weight:600;color:var(--blue);margin-top:16px}
.testi{top:3354px;width:496px;height:256px;background:var(--light)}
.testi .rule{position:absolute;left:62px;top:40px;width:2px;height:176px;background:var(--blue)}
.testi .qmark{position:absolute;left:39px;top:102px;width:48px;height:48px;border-radius:50%;background:var(--blue);border:4px solid #fff;box-shadow:0 0 0 2px var(--blue);display:flex;align-items:center;justify-content:center}
.testi .stars{position:absolute;left:116px;top:46px;color:#e8622a;font-size:16px;letter-spacing:4px}
.testi p{position:absolute;left:116px;top:88px;width:340px;font-size:13px;line-height:23px;color:#555}
.testi h4{position:absolute;left:116px;top:178px;font-size:18px;font-weight:600;color:#1b1b2a}
.testi small{position:absolute;left:116px;top:206px;font-size:12px;color:#555}
.testi .avatar{position:absolute;left:398px;top:172px;width:56px;height:56px;border-radius:50%}
.dots{left:565px;top:3656px;display:flex;gap:9px}
.dots span{width:10px;height:10px;border-radius:50%;background:#d9dae0}
.dots span.on{background:#fff;border:2px solid #e8622a}

/* footer */
.footer{left:0;top:3700px;width:1200px;height:539px;background:var(--footer)}
.foot-wave{left:0;top:3665px;width:1200px;height:95px}
.f-logo{left:126px;top:3800px}
.f-about{left:126px;top:3892px;width:290px;font-size:12px;line-height:22px;color:#9d9ab2}
.socials{left:126px;top:3961px;display:flex;gap:10px}
.socials span{width:28px;height:28px;background:#3a3560;border-radius:3px}
.socials span:first-child{background:var(--red)}
.f-col h4{font-size:14px;font-weight:600;color:#fff;margin-bottom:20px}
.f-col ul{list-style:none}
.f-col li{font-size:12.5px;color:#aaa7bf;line-height:26px}
.news-input{left:826px;top:3918px;width:244px;height:48px;background:#fff;font-size:11px;color:#888;padding:17px 24px}
.news-btn{left:1022px;top:3918px;width:48px;height:48px;background:var(--red);display:flex;align-items:center;justify-content:center}
.f-info{top:4070px;display:flex;gap:16px;align-items:center}
.f-info .ico{width:46px;height:46px;border-radius:50%;background:#3a3560;display:flex;align-items:center;justify-content:center;flex-shrink:0}
.f-info .ico.red{background:var(--red)}
.f-info strong{display:block;color:#fff;font-size:14px;font-weight:600}
.f-info small{display:block;color:#aaa7bf;font-size:11px;margin-top:3px;white-space:nowrap}
.f-rule{left:126px;top:4190px;width:948px;height:1px;background:#332e52}
.copyright{left:0;top:4210px;width:1200px;text-align:center;font-size:12px;color:#fff;letter-spacing:.3px}
</style>
</head>
<body>

<!-- HEADER -->
<div class="abs topbar"></div>
<div class="abs topbar-white"></div>
<div class="abs topbar-info" style="left:466px">
  <svg width="9" height="11" viewBox="0 0 9 11"><path d="M4.5 0A4 4 0 0 0 .5 4c0 3 4 7 4 7s4-4 4-7a4 4 0 0 0-4-4zm0 5.5a1.5 1.5 0 1 1 0-3 1.5 1.5 0 0 1 0 3z" fill="#fff"/></svg>
  48 Larkspur Lane, CA, 95012
</div>
<div class="abs topbar-info" style="left:706px">Follow Us:
  <span style="width:6px;height:6px;background:#dfe3ee;border-radius:50%;margin-left:8px"></span>
  <span style="width:6px;height:6px;background:#dfe3ee;border-radius:50%"></span>
  <span style="width:6px;height:6px;background:#dfe3ee;border-radius:50%"></span>
</div>
<div class="abs quote-link">GET QUOTATION</div>
<div class="abs navbar"></div>
<div class="abs logo">
  <span class="logo-name">VELRO</span>
  <span class="logo-sub">VELMONT ORTHOPEDIC</span>
</div>
<nav class="abs nav">
  <a class="active" href="#" style="margin-right:78px">Home</a>
  <a href="#" style="margin-right:36px">About Us</a>
  <a href="#" style="margin-right:36px">Conditions</a>
  <a href="#" style="margin-right:56px">Services</a>
  <a href="#" style="margin-right:45px">Gallery</a>
  <a href="#" style="margin-right:55px">Team</a>
  <a href="#">Contact Us</a>
</nav>

<!-- HERO -->
<div class="abs hero" role="img" aria-label="Orthopedic specialist holding a tablet in a bright clinic treatment room"></div>
<div class="abs hero-shade"></div>
<div class="abs hero-kicker">ORTHOPEDIC CARE</div>
<h1 class="abs hero-title">Embracing Mobility, Celebrating Life</h1>
<p class="abs hero-text">Lorem ipsum dolor sit amet, consectetur adipiscing elit, sed do eiusmod tempor incididunt ut labore et dolore magna aliqua.</p>
<div class="abs btn" style="left:105px;top:557px">Contact us
  <svg width="16" height="12" viewBox="0 0 16 12"><path d="M1 6h13M9 1l5 5-5 5" stroke="#fff" stroke-width="1.6" fill="none"/></svg>
</div>
<svg class="abs hero-wave" viewBox="0 0 1200 60" preserveAspectRatio="none">
  <path d="M0 30 C300 70 700 20 1200 5 L1200 60 L0 60Z" fill="var(--red)"/>
  <path d="M0 40 C300 80 700 40 1200 30 L1200 60 L0 60Z" fill="#fff"/>
</svg>

<!-- ABOUT -->
<svg class="abs about-photo" viewBox="0 0 464 464" role="img" aria-label="Doctor examining a spine X-ray film">
  <defs><linearGradient id="xr" x1="0" y1="0" x2="1" y2="1"><stop offset="0" stop-color="#d9e0e6"/><stop offset=".5" stop-color="#8c99a8"/><stop offset="1" stop-color="#3d4658"/></linearGradient></defs>
  <circle cx="232" cy="232" r="222" fill="url(#xr)"/>
  <path d="M232 4 A228 228 0 0 1 440 330" stroke="var(--blue)" stroke-width="5" fill="none"/>
  <path d="M24 150 A228 228 0 0 1 232 4" stroke="var(--blue)" stroke-width="5" fill="none"/>
  <path d="M300 450 A228 228 0 0 1 40 340" stroke="var(--blue)" stroke-width="2" fill="none"/>
</svg>
<div class="abs about-copy">
  <span class="eyebrow">Who we are</span>
  <h2>The team you can trust to get the job done</h2>
  <p class="lead">No fear when your expert is a call away</p>
  <p class="body">Lorem ipsum dolor sit amet, consectetur adipiscing elit, sed do eiusmod temp or incididunt ut labore et dolore magna aliqua. Ut enim ad minim veniam, quis laboris nisi ut aliquip ex ea commodo consequat.</p>
  <p class="body">Lorem ipsum dolor sit amet, consectetur adipiscing elit, sed do eiusmod temp or incididunt ut labore et dolore magna aliqua.</p>
</div>
<div class="abs btn" style="left:612px;top:1231px">Contact us
  <svg width="16" height="12" viewBox="0 0 16 12"><path d="M1 6h13M9 1l5 5-5 5" stroke="#fff" stroke-width="1.6" fill="none"/></svg>
</div>

<!-- SERVICES -->
<div class="abs svc-band" role="img" aria-label="Dim clinic scene with a doctor consulting a patient"></div>
<div class="abs svc-label">SERVICES</div>
<h2 class="abs svc-title">Services We Provide</h2>
<div class="abs more-svc">More Services <span class="box"><svg width="8" height="12" viewBox="0 0 8 12"><path d="M2 1l5 5-5 5" stroke="#2fa8b8" stroke-width="1.8" fill="none"/></svg></span></div>

<div class="abs card" style="left:86px">
  <div class="card-img" role="img" aria-label="Doctor examining a patient's lower back" style="background:linear-gradient(120deg,#b7bcc6,#e6e4e0 50%,#8d98a8)"></div>
  <div class="card-icon"><svg width="24" height="24" viewBox="0 0 24 24"><path d="M12 3l2.6 5.6 6 .7-4.5 4.1 1.2 6L12 16.4 6.7 19.4l1.2-6L3.4 9.3l6-.7z" stroke="#fff" stroke-width="1.6" fill="none"/></svg></div>
  <h3>Joint Replacement</h3>
  <p>Lorem ipsum dolor sit amet, conse or incididunt ut labore et .</p>
</div>
<div class="abs card" style="left:436px">
  <div class="card-img" role="img" aria-label="Knee with highlighted joint pain area" style="background:linear-gradient(120deg,#3a4e7a,#c9726a 50%,#2b3d66)"></div>
  <div class="card-icon"><svg width="24" height="24" viewBox="0 0 24 24"><circle cx="12" cy="12" r="8" stroke="#fff" stroke-width="1.6" fill="none"/><path d="M8 12h8M12 8v8" stroke="#fff" stroke-width="1.6"/></svg></div>
  <h3>Diagnostic Imaging</h3>
  <p>Lorem ipsum dolor sit amet, conse or incididunt ut labore et .</p>
</div>
<div class="abs card" style="left:790px">
  <div class="card-img" role="img" aria-label="Senior patient exercising with a physiotherapist" style="background:linear-gradient(120deg,#dfe6ea,#9fb3bd 50%,#e9ecef)"></div>
  <div class="card-icon"><svg width="24" height="24" viewBox="0 0 24 24"><circle cx="12" cy="12" r="8" stroke="#fff" stroke-width="1.6" fill="none"/><circle cx="9" cy="10.5" r="1" fill="#fff"/><circle cx="15" cy="10.5" r="1" fill="#fff"/><path d="M8.5 15.5h7" stroke="#fff" stroke-width="1.6"/></svg></div>
  <h3>Surgical Procedures</h3>
  <p>Lorem ipsum dolor sit amet, conse or incididunt ut labore et .</p>
</div>

<!-- WHY CHOOSE US -->
<div class="abs why-head">
  <span class="eyebrow">Why choose us</span>
  <h2>Why Choose Us</h2>
</div>
<svg class="abs" style="left:403px;top:2156px" width="396" height="396" viewBox="0 0 396 396" role="img" aria-label="Smiling orthopedic doctor with arms crossed">
  <circle cx="198" cy="198" r="198" fill="#eeeff5"/>
  <circle cx="198" cy="198" r="162" fill="#dcdcf3"/>
  <circle cx="198" cy="198" r="152" fill="#8f939c"/>
</svg>

<div class="abs why-item" style="left:79px;top:2178px"><h4 style="left:48px">Collaborative Care</h4><p style="left:48px">Lorem ipsum dolor sit amet, consectetur adipiscing</p></div>
<div class="abs why-item" style="left:80px;top:2324px"><h4 style="left:51px">Collaborative Care</h4><p style="left:51px">Lorem ipsum dolor sit amet, consectetur adipiscing</p></div>
<div class="abs why-item" style="left:79px;top:2474px"><h4 style="left:48px">Minimally Invasive</h4><p style="left:48px">Lorem ipsum dolor sit amet, consectetur adipiscing</p></div>
<div class="abs why-item" style="left:797px;top:2178px"><h4 style="left:45px">Proven Track Record</h4><p style="left:45px">Lorem ipsum dolor sit amet, consectetur adipiscing</p></div>
<div class="abs why-item" style="left:797px;top:2324px"><h4 style="left:71px">Convenient Locations</h4><p style="left:71px">Lorem ipsum dolor sit amet, consectetur adipiscing</p></div>
<div class="abs why-item" style="left:797px;top:2474px"><h4 style="left:48px">Insurance Coordination</h4><p style="left:48px">Lorem ipsum dolor sit amet, consectetur adipiscing</p></div>

<div class="abs why-icon" style="left:375px;top:2199px"><svg width="28" height="28" viewBox="0 0 28 28"><circle cx="14" cy="9" r="5" stroke="var(--red)" stroke-width="1.6" fill="none"/><path d="M5 24c0-5 4-8 9-8s9 3 9 8z" stroke="var(--red)" stroke-width="1.6" fill="none"/></svg></div>
<div class="abs why-icon" style="left:350px;top:2346px"><svg width="28" height="28" viewBox="0 0 28 28"><path d="M9 24V11a2 2 0 0 1 4 0V6a2 2 0 0 1 4 0v6a2 2 0 0 1 4 0v6c0 4-3 6-6 6z" stroke="var(--red)" stroke-width="1.6" fill="none"/></svg></div>
<div class="abs why-icon" style="left:375px;top:2496px"><svg width="28" height="28" viewBox="0 0 28 28"><circle cx="14" cy="14" r="9" stroke="var(--red)" stroke-width="1.6" fill="none"/><path d="M10 14l3 3 5-6" stroke="var(--red)" stroke-width="1.6" fill="none"/></svg></div>
<div class="abs why-icon" style="left:756px;top:2199px"><svg width="28" height="28" viewBox="0 0 28 28"><path d="M14 4l3 6.2 6.6.8-4.9 4.5 1.3 6.6L14 18.8 8 22.1l1.3-6.6-4.9-4.5 6.6-.8z" stroke="var(--red)" stroke-width="1.6" fill="none"/></svg></div>
<div class="abs why-icon" style="left:781px;top:2346px"><svg width="28" height="28" viewBox="0 0 28 28"><path d="M14 4a6 6 0 0 0-6 6c0 5 6 11 6 11s6-6 6-11a6 6 0 0 0-6-6z" stroke="var(--red)" stroke-width="1.6" fill="none"/><circle cx="14" cy="10" r="2" fill="var(--red)"/><path d="M6 24h16" stroke="var(--red)" stroke-width="1.6"/></svg></div>
<div class="abs why-icon" style="left:756px;top:2496px"><svg width="28" height="28" viewBox="0 0 28 28"><circle cx="14" cy="14" r="4" stroke="var(--red)" stroke-width="1.6" fill="none"/><circle cx="14" cy="14" r="9" stroke="var(--red)" stroke-width="1.6" stroke-dasharray="4 3" fill="none"/></svg></div>

<!-- CONTACT -->
<div class="abs contact-band" role="img" aria-label="Technician working with orthopedic equipment in a lab"></div>
<h2 class="abs contact-title">CONTACT US</h2>
<p class="abs contact-sub">Fill out t the form below to get connected with us.</p>
<div class="abs contact-row" style="top:2826px">
  <div class="ico"><svg width="22" height="22" viewBox="0 0 24 24"><path d="M6 3l3 4-2 2c1 3 4 6 7 7l2-2 4 3-2 4C10 21 3 14 3 5z" stroke="var(--red)" stroke-width="1.5" fill="none"/></svg></div>
  <div><small>Our Phone Number:</small><strong>555 014 2267</strong></div>
</div>
<div class="abs contact-row" style="top:2896px">
  <div class="ico"><svg width="22" height="22" viewBox="0 0 24 24"><path d="M12 2a7 7 0 0 0-7 7c0 6 7 13 7 13s7-7 7-13a7 7 0 0 0-7-7z" stroke="var(--red)" stroke-width="1.5" fill="none"/><circle cx="12" cy="9" r="2.5" stroke="var(--red)" stroke-width="1.5" fill="none"/></svg></div>
  <div><small>Our Location:</small><strong>48 Larkspur Lane, Suite 210<br>Velmont, CA</strong></div>
</div>
<div class="abs contact-row" style="top:2976px">
  <div class="ico"><svg width="22" height="22" viewBox="0 0 24 24"><rect x="3" y="6" width="18" height="13" rx="1" stroke="var(--red)" stroke-width="1.5" fill="none"/><path d="M3 7l9 7 9-7" stroke="var(--red)" stroke-width="1.5" fill="none"/></svg></div>
  <div><small>Our Email Address:</small><strong>hello@velmontortho.net</strong></div>
</div>
<div class="abs form-box">
  <div class="field" style="top:24px">Full Name</div>
  <div class="field" style="top:72px">Email Address</div>
  <div class="field" style="top:120px">Phone Number</div>
  <div class="field" style="top:168px;height:114px">Message</div>
  <div class="submit">SUBMIT</div>
</div>

<!-- TESTIMONIALS -->
<div class="abs testi-head">
  <span class="eyebrow">Testimonials</span>
  <h2>What our clients are saying</h2>
</div>
<div class="abs testi" style="left:92px">
  <div class="rule"></div>
  <div class="qmark"><svg width="20" height="16" viewBox="0 0 20 16"><path d="M2 14V8c0-4 2-6 6-7v3c-2 1-3 2-3 4h3v6zM11 14V8c0-4 2-6 6-7v3c-2 1-3 2-3 4h3v6z" fill="#fff"/></svg></div>
  <div class="stars">★★★★★</div>
  <p>Lorem ipsum dolor sit amet, consectetur adipiscing elit, sed do eiusmod tempor incididunt ut labore et dolore magna aliqua. Ut enim</p>
  <h4>Maren Holt</h4>
  <small>Green Valley</small>
  <div class="avatar" role="img" aria-label="Client portrait" style="background:linear-gradient(135deg,#c7c9cf,#7c8089)"></div>
</div>
<div class="abs testi" style="left:614px">
  <div class="rule"></div>
  <div class="qmark"><svg width="20" height="16" viewBox="0 0 20 16"><path d="M2 14V8c0-4 2-6 6-7v3c-2 1-3 2-3 4h3v6zM11 14V8c0-4 2-6 6-7v3c-2 1-3 2-3 4h3v6z" fill="#fff"/></svg></div>
  <div class="stars">★★★★★</div>
  <p>Lorem ipsum dolor sit amet, consectetur adipiscing elit, sed do eiusmod tempor incididunt ut labore et dolore magna aliqua. Ut enim</p>
  <h4>Maren Holt</h4>
  <small>Green Valley</small>
  <div class="avatar" role="img" aria-label="Client portrait" style="background:linear-gradient(135deg,#e6d9c6,#6a5b4e)"></div>
</div>
<div class="abs dots"><span></span><span></span><span class="on"></span><span></span></div>

<!-- FOOTER -->
<div class="abs footer"></div>
<svg class="abs foot-wave" viewBox="0 0 1200 95" preserveAspectRatio="none">
  <path d="M0 95 L0 55 C350 -10 750 80 1200 5 L1200 95Z" fill="var(--red)"/>
  <path d="M0 95 L0 80 C350 20 750 95 1200 30 L1200 95Z" fill="var(--footer)"/>
</svg>
<div class="abs f-logo" style="display:flex;flex-direction:column">
  <span class="logo-name" style="color:#fff;font-size:50px;letter-spacing:10px">VELRO</span>
  <span class="logo-sub" style="color:#fff;font-size:11px;letter-spacing:2.4px">VELMONT ORTHOPEDIC</span>
</div>
<p class="abs f-about">Lorem ipsum dolor sit amet, consectetur adipiscing elit, sed do eiusmod tempor incididunt ut</p>
<div class="abs socials"><span></span><span></span><span></span><span></span></div>

<div class="abs f-col" style="left:489px;top:3820px">
  <h4>Quick Links</h4>
  <ul><li>Home</li><li>Services</li><li>About Us</li><li>Contact</li><li>Blog</li><li>Testimonials</li></ul>
</div>
<div class="abs f-col" style="left:625px;top:3866px">
  <ul><li>Cookies Policy</li><li>Terms of Use</li><li>Careers</li><li>Our Team</li><li>More</li></ul>
</div>
<div class="abs f-col" style="left:826px;top:3820px;width:250px">
  <h4>Newsletters</h4>
  <p style="font-size:11.5px;line-height:21px;color:#aaa7bf;margin-top:-6px">Lorem ipsum dolor sit amet, consectetur adi piscing elit, sed do eiusmod tempor</p>
</div>
<div class="abs news-input">Enter Email Address</div>
<div class="abs news-btn"><svg width="12" height="16" viewBox="0 0 12 16"><path d="M3 2l6 6-6 6" stroke="#fff" stroke-width="2.2" fill="none"/></svg></div>

<div class="abs f-info" style="left:126px">
  <div class="ico"><svg width="18" height="20" viewBox="0 0 24 24"><path d="M12 2a7 7 0 0 0-7 7c0 6 7 13 7 13s7-7 7-13a7 7 0 0 0-7-7z" fill="#8a85a8"/><circle cx="12" cy="9" r="2.5" fill="#3a3560"/></svg></div>
  <div><strong>Address</strong><small>48 Larkspur Lane</small></div>
</div>
<div class="abs f-info" style="left:364px">
  <div class="ico red"><svg width="20" height="18" viewBox="0 0 24 24"><rect x="3" y="6" width="18" height="13" rx="1" fill="#fff"/><path d="M3 7l9 7 9-7" stroke="var(--red)" stroke-width="1.5" fill="none"/></svg></div>
  <div><strong>Email Us</strong><small>care@velmontortho.net</small></div>
</div>
<div class="abs f-info" style="left:632px">
  <div class="ico"><svg width="18" height="18" viewBox="0 0 24 24"><path d="M6 3l3 4-2 2c1 3 4 6 7 7l2-2 4 3-2 4C10 21 3 14 3 5z" fill="#8a85a8"/></svg></div>
  <div><strong>Contact Us</strong><small>+1 (555) 014 2267</small></div>
</div>
<div class="abs f-info" style="left:860px">
  <div class="ico"><svg width="20" height="20" viewBox="0 0 24 24"><circle cx="12" cy="12" r="8" stroke="#8a85a8" stroke-width="1.8" fill="none"/><path d="M12 7v5l3 2" stroke="#8a85a8" stroke-width="1.8" fill="none"/></svg></div>
  <div><strong>Opening Hour</strong><small>Mon - Friday 10 am - 8pm</small></div>
</div>
<div class="abs f-rule"></div>
<div class="abs copyright">VELMONT ORTHOPEDICS</div>

</body>
</html>
```